Card design for orthopaedic surgeons working as The Brindlewood Orthopaedic Centre

Business cards, letterhead

Colors

Designer to choose colors to be used in the design.

Requirements
Must have
• Late addition.
• Cards letterhead must have logos of
• Corvane Federated Institute of Surgeons
• Meridale Orthopaedic Society
Nice to have
• Back of card to have space for appointment time to be added by hand and some blank space for writing incidental other notes.

```html
<!DOCTYPE html>
<html lang="en">
<head>
<meta charset="utf-8">
<title>The Brindlewood Orthopaedic Centre – Business Card</title>
<link rel="stylesheet" href="https://fonts.googleapis.com/css2?family=Lato:wght@300;400&family=Montserrat:wght@700&display=swap">
<style>
  :root {
    --page-bg: #2a2b2d;
    --card-bg: #0a0b0b;
    --brand-blue: #4fa3dc;
    --text-white: #ffffff;
    --icon-grey: #e6e6e6;
  }
  * { margin: 0; padding: 0; box-sizing: border-box; }
  html, body {
    width: 1200px;
    height: 970px;
    overflow: hidden;
    background: var(--page-bg);
  }
  .canvas {
    position: relative;
    width: 1200px;
    height: 970px;
  }
  .card {
    position: absolute;
    left: 230px;
    width: 740px;
    height: 420px;
    background: var(--card-bg);
    border-bottom: 5px solid var(--brand-blue);
    box-shadow: 0 10px 24px rgba(0, 0, 0, 0.55);
    font-family: "Lato", sans-serif;
  }
  .card--front { top: 50px; }
  .card--back { top: 510px; }

  .brand-name {
    position: absolute;
    font-family: "Lato", sans-serif;
    font-weight: 300;
    color: var(--brand-blue);
    white-space: nowrap;
    letter-spacing: 0.2px;
  }
  .card--front .brand-name {
    left: 60px;
    top: 62px;
    font-size: 33px;
  }
  .card--back .brand-name {
    left: 0;
    right: 0;
    top: 178px;
    text-align: center;
    font-size: 40px;
  }

  .person {
    position: absolute;
    right: 56px;
    top: 190px;
    text-align: right;
  }
  .person__name {
    font-family: "Montserrat", sans-serif;
    font-weight: 700;
    font-size: 28px;
    color: var(--text-white);
    letter-spacing: 0.5px;
  }
  .person__role {
    font-size: 18px;
    color: var(--brand-blue);
    margin-top: 2px;
  }

  .address {
    position: absolute;
    left: 96px;
    top: 232px;
    font-size: 18px;
    line-height: 24px;
    color: var(--brand-blue);
  }
  .contact-list {
    position: absolute;
    left: 96px;
    top: 300px;
    list-style: none;
  }
  .contact-list__item {
    display: flex;
    align-items: center;
    gap: 14px;
    height: 28px;
    font-size: 18px;
    color: var(--brand-blue);
  }
  .contact-list__icon {
    width: 18px;
    height: 18px;
    flex: none;
  }
</style>
</head>
<body>
<main class="canvas">

  <section class="card card--front" aria-label="Business card front">
    <p class="brand-name">The Brindlewood Orthopaedic Centre</p>

    <div class="person">
      <p class="person__name">JOHN SMITH</p>
      <p class="person__role">Founder &amp; CEO</p>
    </div>

    <p class="address">1234 First Line Address<br>5678 Second Line Address</p>

    <ul class="contact-list">
      <li class="contact-list__item">
        <svg class="contact-list__icon" viewBox="0 0 24 24" aria-hidden="true">
          <path d="M6.6 10.8a15 15 0 0 0 6.6 6.6l2.2-2.2a1 1 0 0 1 1-.25 11.4 11.4 0 0 0 3.6.57 1 1 0 0 1 1 1V20a1 1 0 0 1-1 1A17 17 0 0 1 3 4a1 1 0 0 1 1-1h3.5a1 1 0 0 1 1 1c0 1.25.2 2.45.57 3.57a1 1 0 0 1-.25 1z" fill="var(--icon-grey)"/>
        </svg>
        <span>1234567890</span>
      </li>
      <li class="contact-list__item">
        <svg class="contact-list__icon" viewBox="0 0 24 24" aria-hidden="true">
          <rect x="2" y="5" width="20" height="14" fill="none" stroke="var(--icon-grey)" stroke-width="2"/>
          <path d="M2 5l10 8 10-8" fill="none" stroke="var(--icon-grey)" stroke-width="2"/>
        </svg>
        <span>info@yourmail.com</span>
      </li>
      <li class="contact-list__item">
        <svg class="contact-list__icon" viewBox="0 0 24 24" aria-hidden="true">
          <circle cx="12" cy="12" r="10" fill="none" stroke="var(--icon-grey)" stroke-width="1.8"/>
          <ellipse cx="12" cy="12" rx="4.5" ry="10" fill="none" stroke="var(--icon-grey)" stroke-width="1.5"/>
          <path d="M2 12h20M4 7h16M4 17h16" stroke="var(--icon-grey)" stroke-width="1.5"/>
        </svg>
        <span>www.yourwebsite.com</span>
      </li>
    </ul>
  </section>

  <section class="card card--back" aria-label="Business card back">
    <p class="brand-name">The Brindlewood Orthopaedic Centre</p>
  </section>

</main>
</body>
</html>
```